Business Card Design Project

I need a business card designed that is clean, simple and elegant.
I am a fashion and advertising photographer based in Cape Town and Durban South Africa.
check out my website: www.marlowvance.co.za for ideas
Updates
Hi all,
Thanks for your submissions so far!
Please note:
I want no more than than black, white and/or grey to be used.
I don't want any photos used.
I would like the card to be double sided.
I would like to continue the design similar to the past ones Ive used.
I hope this helps, please send me further questions should you have any.
many thanks!
Marlow
Hi,
Please have a look at the jpg I loaded(called inspiration) which is the direction or inspiration I am aiming at.
Also PLEASE remember NO PHOTOS to be included on the card
many thanks!!
Target Market(s)
You can look at my site to get a better understanding of the audience:
www.marlowvance.co.za
Industry/Entity Type
Advertising
Requirements
Must have
- Clean design which can also be used for a watermark on photographs
perhaps black background with white text/grey
company called: Marlow Vance Photography
Nice to have
- below I have added logos that I have used in the past.
Should not have
- pictures of cameras
tacky elements

```html
<!DOCTYPE html>
<html lang="en">
<head>
<meta charset="UTF-8">
<title>Marlow Vance Photography – Business Card</title>
<link href="https://fonts.googleapis.com/css2?family=Questrial&display=swap" rel="stylesheet">
<style>
  :root {
    --backdrop: #e4e3e0;
    --card-paper: #f6f6f4;
    --card-edge: #d9d9d6;
    --ink-name: #575757;
    --ink-sub: #6a6a6a;
    --ink-web: #5e5e5e;
    --shadow: rgba(0, 0, 0, 0.18);
  }
  html, body {
    margin: 0;
    padding: 0;
    width: 1200px;
    height: 1023px;
    overflow: hidden;
    background: var(--backdrop);
  }
  .canvas {
    position: relative;
    width: 1200px;
    height: 1023px;
    display: flex;
    align-items: center;
    justify-content: center;
  }
  .business-card {
    position: relative;
    width: 900px;
    height: 514px;
    background: radial-gradient(ellipse at 40% 35%, #fbfbfa 0%, var(--card-paper) 60%, #efefed 100%);
    border: 1px solid var(--card-edge);
    box-shadow: 0 18px 40px var(--shadow), 0 2px 4px rgba(0,0,0,0.08);
    font-family: "Questrial", "Helvetica Neue", Arial, sans-serif;
  }
  .brand {
    position: absolute;
    left: 0;
    right: 0;
    top: 178px;
    text-align: center;
  }
  .brand-name {
    margin: 0;
    font-size: 78px;
    font-weight: 400;
    letter-spacing: 1px;
    line-height: 1;
    color: var(--ink-name);
    text-transform: uppercase;
  }
  .brand-tagline {
    margin: 14px 0 0 0;
    font-size: 24px;
    letter-spacing: 15px;
    color: var(--ink-sub);
    text-transform: uppercase;
    padding-left: 15px;
  }
  .website {
    position: absolute;
    right: 60px;
    bottom: 48px;
    margin: 0;
    font-size: 17px;
    letter-spacing: 6px;
    color: var(--ink-web);
  }
</style>
</head>
<body>
  <main class="canvas">
    <article class="business-card">
      <header class="brand">
        <h1 class="brand-name">Marlow Vance</h1>
        <p class="brand-tagline">Photography</p>
      </header>
      <p class="website">www.marlowvance.co.za</p>
    </article>
  </main>
</body>
</html>
```